Labels/logo for luxury bath products

I am developing a range of luxury bath foams - aimed at the top end of the luxury market. My company name is VEM (very basic website can be seen at www.vemarton.example).

I am looking for a label design for the front of the bottle, which should incorporate the VEM logo as per the website (file attached), but embedded within a more intricate label design. I provide a link to a picture of the bottle below.

The bath foam will come in four fragrances: Vetiver, Sandalwood, Jasmine and Neroli. The label should include the fragrance name. So the label must include the brand name 'VEM' and the name of the fragrance - e.g. Sandalwood Bath Foam, Neroli Bath Foam, etc.

The products are aimed at both the male and female market and so shouldn't be too feminine.

A brand to take inspiration from is Lune Bravière: http://www.lunebraviere.example/ - I like the labels that they use on their products, which is a gold embossed crest, which they use as the label for their products. I am not referring to their font, but to their label design - I like the embossed label, and am quite keen on metallics.

Conversely, I would like to add a contemporary edge to this design - I like the striping and contemporary fonts on this design: http://www.hadley-frost.example/images/fac83.jpg

My brand also harnesses the powers of natural flower ingredients, and so I am inspired by the products of Quenby - quenby.example. This labelling is more clinical and scientific.

Ideally I would like a label which combines these elements - i.e. a luxury label with a contemporary feel, that incorporate the scientific nature of the product.

The design needs to communicate high end luxury. The bottle is however apothecary style, and a nod to science and botany would be good. I would however like a bold approach to this design - it is a modern brand.

The bottle being used for the product can be seen at: http://www.tavel-vitro.example/en/product-groups/8-Apothecary-bottles - these are extremely expensive bottles and the label needs to reflect this quality. These bottles are traditional in design, but incorporate high end glassware technology to preserve the integrity of the natural ingredients. Therefore the product is a mix of old and new, and the label could also reflect this. The colour of the glass is very deep purple.

The front label does not need information such as weight/volume - it purely needs a label which will recognise it as the VEM brand, with the product name. I am looking for a high quality label, which is unique. I am happy to print embossed labels and to use foils on my labels.

Please do not be boring! I appreciate I have given a variety of influences, so summarise the requirements are a mix of:

a bold design
contemporary
luxury

The label must include NO slogans.

I am looking to build a relationship with a graphic designer for packaging and website design requirements so this will be the first of many projects.

Target Market(s)

Luxury end of market - clientele will like luxury and will pay for the highest quality ingredients in the product, but will also appreciate the botanical nature of the product.

Industry/Entity Type

Graphic Designer

Requirements
Must have
• Must include the company name, VEM, although this doesn't need to be particularly prominent. And the product name, e.g. Sandalwood.
Nice to have
• It should combine luxury, but with recognition of the science behind the product.
Should not have
• No slogans, minimal wording on the front label. No other wording other than company name and product name. No primary colours.

```html
<!DOCTYPE html>
<html lang="en">
<head>
<meta charset="utf-8">
<title>VEM Bath Foam Labels</title>
<link href="https://fonts.googleapis.com/css2?family=Great+Vibes&family=Montserrat:wght@800&family=Playfair+Display:wght@400&display=swap" rel="stylesheet">
<style>
  :root {
    --page: #ffffff;
    --label: #050505;
    --ink: #ffffff;
    --sandalwood: #a57f4b;
    --jasmine: #ffffff;
    --vetiver: #33b82c;
    --neroli: #7436e8;
  }
  html, body {
    margin: 0;
    width: 1200px;
    height: 900px;
    overflow: hidden;
    background: var(--page);
  }
  .range {
    width: 1200px;
    height: 900px;
    display: flex;
    justify-content: center;
    align-items: center;
    gap: 100px;
  }
  .label {
    width: 180px;
    height: 470px;
    background: var(--label);
    border-radius: 12px;
    box-sizing: border-box;
    padding: 26px 16px 24px 18px;
    display: flex;
    flex-direction: column;
    color: var(--ink);
  }
  .brand {
    font-family: "Montserrat", sans-serif;
    font-weight: 800;
    font-size: 44px;
    letter-spacing: -1px;
    line-height: 1;
    text-align: center;
    margin: 0 0 22px;
  }
  .label-body {
    flex: 1;
    position: relative;
  }
  .product-name {
    position: absolute;
    left: 0;
    bottom: 0;
    writing-mode: vertical-rl;
    transform: rotate(180deg);
    margin: 0;
    font-weight: 400;
    display: flex;
    flex-direction: column;
    white-space: nowrap;
  }
  .fragrance {
    font-family: "Great Vibes", cursive;
    font-weight: 400;
    font-size: 52px;
    line-height: 1.25;
  }
  .product-type {
    font-family: "Playfair Display", serif;
    font-weight: 400;
    font-size: 22px;
    letter-spacing: 0.5px;
    line-height: 1.15;
    margin-block-start: 6px;
  }
  .bubbles {
    position: absolute;
    top: 0;
    right: 0;
    width: 50px;
    height: 111px;
  }
  .sandalwood .bubbles { fill: var(--sandalwood); }
  .jasmine .bubbles { fill: var(--jasmine); }
  .vetiver .bubbles { fill: var(--vetiver); }
  .neroli .bubbles { fill: var(--neroli); }
</style>
</head>
<body>
<main class="range">
  <article class="label sandalwood">
    <p class="brand">VEM</p>
    <div class="label-body">
      <h2 class="product-name"><span class="fragrance">Sandalwood</span><span class="product-type">BATH FOAM</span></h2>
      <svg class="bubbles" viewBox="0 0 54 120" aria-hidden="true">
        <circle cx="27" cy="22" r="22"/><circle cx="27" cy="62" r="19"/><circle cx="27" cy="96" r="14"/>
      </svg>
    </div>
  </article>
  <article class="label jasmine">
    <p class="brand">VEM</p>
    <div class="label-body">
      <h2 class="product-name"><span class="fragrance">Jasmine</span><span class="product-type">BATH FOAM</span></h2>
      <svg class="bubbles" viewBox="0 0 54 120" aria-hidden="true">
        <circle cx="27" cy="22" r="22"/><circle cx="27" cy="62" r="19"/><circle cx="27" cy="96" r="14"/>
      </svg>
    </div>
  </article>
  <article class="label vetiver">
    <p class="brand">VEM</p>
    <div class="label-body">
      <h2 class="product-name"><span class="fragrance">Vetiver</span><span class="product-type">BATH FOAM</span></h2>
      <svg class="bubbles" viewBox="0 0 54 120" aria-hidden="true">
        <circle cx="27" cy="22" r="22"/><circle cx="27" cy="62" r="19"/><circle cx="27" cy="96" r="14"/>
      </svg>
    </div>
  </article>
  <article class="label neroli">
    <p class="brand">VEM</p>
    <div class="label-body">
      <h2 class="product-name"><span class="fragrance">Neroli</span><span class="product-type">BATH FOAM</span></h2>
      <svg class="bubbles" viewBox="0 0 54 120" aria-hidden="true">
        <circle cx="27" cy="22" r="22"/><circle cx="27" cy="62" r="19"/><circle cx="27" cy="96" r="14"/>
      </svg>
    </div>
  </article>
</main>
</body>
</html>
```